Sudsy Harbor Laundromat Wordpress Design

We need a Wordpress website design for our laundromat, Sudsy Harbor Atlanta, at www.sudsyharborlaunder.example. We would like to have 6 pages: Home, About Us, Services, Locations, Reviews and Contact us. We will provide content for the text on each page. What we do: We are a full service laundromat that provides dry cleaning drop off, professional laundry services, wash dry fold and self service laundry to the local community. We would like to use the color scheme from our logo to convey a warm, safe, and bright business that caters to its diverse community.
Updates

I like the structure of this laundromat website: http://www.tumblewashexample.com/ Using my logo and color scheme in the above referenced website is what. Am looking for. The photos attached to the project with the female model should be used as a primary focus and supplemented by actual photos of the equipment.

Target Market(s)

Our target market is a diverse group of people from Midtown Atlanta - LGBTQ community /Locals/Regulars that have been coming to laundromat for 30 years.

Industry/Entity Type

Laundromat

Coding

Coded - Design and coding required

Number of Pages Required

5+ page

Font styles to use
Sans Serif

Colors
0054AA
0677BA
7BADD7
CADEEF
E8F1F8

Requirements
Must have
• Feature this video on the main page: https://videos.example.net/wq7PzrT2kLm

```html
<!DOCTYPE html>
<html lang="en">
<head>
<meta charset="utf-8">
<title>Sudsy Harbor Laundromat</title>
<link rel="stylesheet" href="https://fonts.googleapis.com/css2?family=Inter:ital,wght@0,400;0,500;0,600;0,700;1,400&family=Lobster&display=swap">
<style>
:root{
  --navy:#00336b;
  --blue:#0054aa;
  --mid:#1d63b0;
  --sky:#1a9bd7;
  --pale:#f4f5f7;
  --foot:#defcfd;
  --text:#1b2a3a;
  --muted:#7a8594;
  --white:#ffffff;
}
*{box-sizing:border-box;margin:0;padding:0}
html,body{width:1200px;height:2807px;overflow:hidden}
body{position:relative;font-family:"Inter",sans-serif;color:var(--text);background:var(--pale)}
.abs{position:absolute}
.script{font-family:"Lobster",cursive;font-weight:400}

/* header */
.site-header{left:0;top:0;width:1200px;height:94px;background:var(--white);z-index:3}
.brand{left:87px;top:26px;display:flex;align-items:center;gap:10px;font-size:24px;font-weight:600;color:var(--blue)}
.brand-dot{width:14px;height:14px;border-radius:50%;background:var(--sky)}
.main-nav{left:508px;top:40px;display:flex;font-size:12px;font-weight:500}
.main-nav a{color:var(--text);text-decoration:none;margin-right:21px}
.main-nav a.current{color:var(--sky)}
.header-phone{left:858px;top:36px;display:flex;align-items:center;gap:8px;font-size:15px;font-style:italic;font-weight:700;color:var(--blue)}
.btn{display:flex;align-items:center;justify-content:center;border:1px solid var(--sky);font-size:12px;font-weight:500;color:var(--blue);background:var(--white);box-shadow:2px 2px 0 -1px var(--blue)}
.header-cta{left:1000px;top:27px;width:112px;height:38px;color:var(--sky)}

/* hero */
.hero{left:0;top:94px;width:1200px;height:640px;background:linear-gradient(180deg,#6f7a82 0%,#8b9094 45%,#5c6064 100%)}
.hero-title{left:0;top:396px;width:1175px;text-align:center;font-size:38px;color:var(--white)}
.hero-sub{left:340px;top:442px;width:495px;text-align:center;font-size:22px;line-height:27px;color:var(--white)}
.wave{left:0;width:1200px}
.down-arrow{left:590px;top:553px}

/* services */
.section-title{left:0;width:1200px;text-align:center;color:var(--blue);font-size:37px}
.service{width:260px;text-align:center}
.service-photo{width:200px;height:200px;border-radius:50%;margin:0 auto;border:1px solid var(--sky);padding:5px}
.service-photo span{display:block;width:100%;height:100%;border-radius:50%}
.service h3{margin-top:20px;font-size:15px;font-weight:600;color:var(--blue)}
.service p{margin:15px auto 0;width:248px;font-size:10px;line-height:15px;color:var(--muted)}
.service .btn{width:112px;height:38px;margin:23px auto 0}

/* about */
.about{left:0;top:1232px;width:1200px;height:460px;background:var(--navy)}
.about-title{left:87px;top:1312px;font-size:35px;line-height:53px;color:var(--white)}
.about-text{left:87px;top:1427px;width:640px;font-size:10.5px;line-height:15px;color:var(--white)}
.checks{top:1490px;list-style:none;font-size:11.5px;font-weight:600;color:var(--white)}
.checks li{display:flex;align-items:center;gap:9px;height:19px}
.about-btn{left:87px;top:1591px;width:113px;height:37px;background:transparent;color:var(--white);border-color:var(--white);box-shadow:2px 2px 0 -1px var(--sky)}
.video-frame{left:775px;top:1295px;width:337px;height:336px;border:1px solid var(--sky)}
.video{left:750px;top:1320px;width:338px;height:337px;background:linear-gradient(135deg,#8d8a77 0%,#b9b6aa 45%,#6d6a5c 100%)}
.play{left:902px;top:1471px}

/* reviews */
.review{top:1972px;width:250px;height:275px;background:var(--white);box-shadow:0 4px 18px rgba(0,40,90,.08);padding:30px 18px 0}
.quote-mark{font-size:26px;line-height:24px;color:var(--sky);font-weight:500;letter-spacing:1px}
.review p{margin-top:14px;font-size:10.5px;line-height:18.7px;font-style:italic;color:var(--muted)}
.review h4{margin-top:16px;font-size:11.5px;font-weight:600;color:var(--blue)}
.review small{display:block;font-size:10.5px;color:var(--muted);margin-top:3px}

/* footer */
.footer{left:0;top:2420px;width:1200px;height:387px;background:var(--foot)}
.foot-brand{left:199px;top:2575px;display:flex;align-items:center;gap:10px;font-size:22px;font-weight:600;color:var(--blue)}
.foot-head{top:2550px;font-size:16px;color:var(--navy)}
.foot-line{display:flex;align-items:flex-start;gap:10px;font-size:11px;line-height:15px;color:var(--text)}
.foot-links{left:668px;top:2582px;list-style:none;font-size:10.5px;line-height:18.7px}
.newsletter-text{left:817px;top:2581px;width:190px;font-size:10px;line-height:15px}
.email-field{left:817px;top:2626px;width:182px;height:24px;background:#5e7c99;color:#e6eef6;font-size:9px;padding:7px 12px}
.send{left:818px;top:2662px;width:101px;height:25px;color:var(--sky)}
.divider{left:200px;top:2737px;width:799px;height:1px;background:#b9d5df}
.copy{left:200px;top:2762px;font-size:9.5px;color:var(--muted)}
.copy b{color:var(--blue);font-weight:600}
.social{top:2756px;width:24px;height:24px;border-radius:50%}
</style>
</head>
<body>

<header class="abs site-header">
  <div class="abs brand"><span>Sudsy Harbor</span><span class="brand-dot"></span></div>
  <nav class="abs main-nav">
    <a class="current" href="#">Home</a><a href="#">About Us</a><a href="#">Services</a><a href="#">Locations</a><a href="#">Reviews</a>
  </nav>
  <div class="abs header-phone">
    <svg width="16" height="16" viewBox="0 0 24 24" fill="none" stroke="#0054aa" stroke-width="2"><path d="M5 3h4l2 5-3 2a12 12 0 0 0 6 6l2-3 5 2v4a2 2 0 0 1-2 2A18 18 0 0 1 3 5a2 2 0 0 1 2-2z"/></svg>
    404-555-0187
  </div>
  <a class="abs btn header-cta">Contact Us</a>
</header>

<section class="abs hero" role="img" aria-label="Photo of a retro laundromat with a model in a blue dress walking past rows of washers"></section>
<h1 class="abs hero-title script">Laundromat for 30 Years</h1>
<p class="abs hero-sub">Coin Laundry, Dry Cleaning, and Professional Laundry</p>

<svg class="abs wave" style="top:480px" width="1200" height="260" viewBox="0 0 1200 260" preserveAspectRatio="none">
  <path d="M0 185 C250 20 420 30 650 150 C820 230 1000 150 1200 0 L1200 260 L0 260Z" fill="#f4f5f7"/>
  <path d="M0 205 C260 60 430 70 660 175 C840 245 1020 190 1200 50 L1200 80 C1020 215 840 275 660 215 C430 120 250 110 0 255Z" fill="#1d63b0"/>
</svg>
<svg class="abs down-arrow" width="20" height="26" viewBox="0 0 20 26" fill="none" stroke="#1b2a3a" stroke-width="1.6"><path d="M10 1v23M2 16l8 8 8-8"/></svg>

<h2 class="abs section-title script" style="top:735px">What We Do</h2>

<div class="abs service" style="left:195px;top:802px">
  <div class="service-photo"><span role="img" aria-label="Model leaning against a front-loading washer" style="background:linear-gradient(135deg,#c9d3d8,#b0704a 70%,#2f5fa6)"></span></div>
  <h3>Dry Cleaning Drop Off</h3>
  <p>It is a long established fact that a reader will be distracted by the readable content of a page when looking at its layout. The point of using Lorem Ipsum is that it has a more-or-less normal ...</p>
  <a class="btn">Read More</a>
</div>
<div class="abs service" style="left:470px;top:802px">
  <div class="service-photo"><span role="img" aria-label="Model seated on a chair in front of washing machines" style="background:linear-gradient(180deg,#9aa0a3,#d9d6cf 60%,#3a67ad)"></span></div>
  <h3>Professional Laundry Services</h3>
  <p>It is a long established fact that a reader will be distracted by the readable content of a page when looking at its layout. The point of using Lorem Ipsum is that it has a more-or-less normal ...</p>
  <a class="btn" style="color:var(--sky)">Read More</a>
</div>
<div class="abs service" style="left:745px;top:802px">
  <div class="service-photo"><span role="img" aria-label="Model in a blue dress beneath the laundromat wall sign" style="background:linear-gradient(180deg,#b7c6c7,#cfd1cc 55%,#2c5a9e)"></span></div>
  <h3>Wash Dry Fold</h3>
  <p>It is a long established fact that a reader will be distracted by the readable content of a page when looking at its layout. The point of using Lorem Ipsum is that it has a more-or-less normal ...</p>
  <a class="btn">Read More</a>
</div>

<section class="abs about"></section>
<h2 class="abs about-title script">Coin Laundry, Dry Cleaning, &amp;<br>Professional Laundry</h2>
<p class="abs about-text">There are many variations of passages of Lorem Ipsum available, but the majority have suffered alteration in some form, by injected humour, or randomised words which don't look even slightly believable. If you are going to use a passage of Lorem Ipsum, you need to be sure there isn't anything embarrassing hidden in the middle of text.</p>
<ul class="abs checks" style="left:87px">
  <li><svg width="13" height="9" viewBox="0 0 13 9" fill="none" stroke="#fff" stroke-width="1.3"><path d="M1 5l3 3 8-7M5 5l3-3"/></svg>In Business over 45 years</li>
  <li><svg width="13" height="9" viewBox="0 0 13 9" fill="none" stroke="#fff" stroke-width="1.3"><path d="M1 5l3 3 8-7M5 5l3-3"/></svg>Voted "BEST COIN LAUNDRY" - Multiple years</li>
  <li><svg width="13" height="9" viewBox="0 0 13 9" fill="none" stroke="#fff" stroke-width="1.3"><path d="M1 5l3 3 8-7M5 5l3-3"/></svg>The best Wash-Dry-Fold in town</li>
  <li><svg width="13" height="9" viewBox="0 0 13 9" fill="none" stroke="#fff" stroke-width="1.3"><path d="M1 5l3 3 8-7M5 5l3-3"/></svg>Over 50 well maintained machines</li>
</ul>
<ul class="abs checks" style="left:379px">
  <li><svg width="13" height="9" viewBox="0 0 13 9" fill="none" stroke="#fff" stroke-width="1.3"><path d="M1 5l3 3 8-7M5 5l3-3"/></svg>In Business over 45 years</li>
  <li><svg width="13" height="9" viewBox="0 0 13 9" fill="none" stroke="#fff" stroke-width="1.3"><path d="M1 5l3 3 8-7M5 5l3-3"/></svg>One of Atlanta's First, Finest, &amp; Friendliest Coin Laundries</li>
  <li><svg width="13" height="9" viewBox="0 0 13 9" fill="none" stroke="#fff" stroke-width="1.3"><path d="M1 5l3 3 8-7M5 5l3-3"/></svg>Cool - Comfortable - Clean</li>
  <li><svg width="13" height="9" viewBox="0 0 13 9" fill="none" stroke="#fff" stroke-width="1.3"><path d="M1 5l3 3 8-7M5 5l3-3"/></svg>Commercial Accounts</li>
</ul>
<a class="abs btn about-btn">About Us</a>
<div class="abs video-frame"></div>
<div class="abs video" role="img" aria-label="Video still of a customer carrying a laundry basket at the counter"></div>
<svg class="abs play" width="34" height="34" viewBox="0 0 34 34" fill="none" stroke="#fff" stroke-width="2"><circle cx="17" cy="17" r="15"/><path d="M13 10l11 7-11 7z"/></svg>

<svg class="abs wave" style="top:1680px" width="1200" height="260" viewBox="0 0 1200 260" preserveAspectRatio="none">
  <path d="M0 0 L1200 0 C1000 150 820 230 650 150 C420 30 250 20 0 185Z" fill="#00336b"/>
  <path d="M0 185 C250 20 420 30 650 150 C820 230 1000 150 1200 0 L1200 260 L0 260Z" fill="#f4f5f7"/>
  <path d="M0 205 C260 60 430 70 660 175 C840 245 1020 190 1200 50 L1200 80 C1020 215 840 275 660 215 C430 120 250 110 0 255Z" fill="#1d63b0"/>
</svg>

<h2 class="abs section-title script" style="top:1905px">Client Reviews</h2>

<article class="abs review" style="left:200px">
  <div class="quote-mark">66</div>
  <p>"There are many variations of passages of Lorem Ipsum available, but the majority have suffered alteration in some form, by injected humour, or randomised words which don't look even slightly believable. If you are going to use a passage of Lorem Ipsum, you need to be sure there isn't anything embarrassing"</p>
  <h4>Standard Chunk</h4><small>popular belief</small>
</article>
<article class="abs review" style="left:475px">
  <div class="quote-mark">66</div>
  <p>"There are many variations of passages of Lorem Ipsum available, but the majority have suffered alteration in some form, by injected humour, or randomised words which don't look even slightly believable. If you are going to use a passage of Lorem Ipsum, you need to be sure there isn't anything embarrassing"</p>
  <h4>Standard Chunk</h4><small>popular belief</small>
</article>
<article class="abs review" style="left:750px">
  <div class="quote-mark">66</div>
  <p>"There are many variations of passages of Lorem Ipsum available, but the majority have suffered alteration in some form, by injected humour, or randomised words which don't look even slightly believable. If you are going to use a passage of Lorem Ipsum, you need to be sure there isn't anything embarrassing"</p>
  <h4>Standard Chunk</h4><small>popular belief</small>
</article>

<footer class="abs footer"></footer>
<svg class="abs wave" style="top:2300px" width="1200" height="210" viewBox="0 0 1200 210" preserveAspectRatio="none">
  <path d="M0 150 C260 20 430 30 660 140 C840 200 1020 150 1200 40 L1200 210 L0 210Z" fill="#defcfd"/>
  <path d="M0 150 C260 20 430 30 660 140 C840 200 1020 150 1200 40 L1200 70 C1020 185 840 225 660 180 C430 90 250 80 0 195Z" fill="#1d63b0"/>
</svg>

<div class="abs foot-brand"><span>Sudsy Harbor</span><span class="brand-dot"></span></div>

<h3 class="abs foot-head script" style="left:405px">Contact Us</h3>
<div class="abs foot-line" style="left:407px;top:2584px;font-size:14px">
  <svg width="13" height="13" viewBox="0 0 24 24" fill="none" stroke="#1a9bd7" stroke-width="2"><path d="M5 3h4l2 5-3 2a12 12 0 0 0 6 6l2-3 5 2v4a2 2 0 0 1-2 2A18 18 0 0 1 3 5a2 2 0 0 1 2-2z"/></svg>(404) 555-0187
</div>
<div class="abs foot-line" style="left:407px;top:2606px">
  <svg width="12" height="12" viewBox="0 0 24 24" fill="none" stroke="#1a9bd7" stroke-width="2"><rect x="3" y="5" width="18" height="14"/><path d="M3 6l9 7 9-7"/></svg>hello@sudsyharbor.example
</div>
<div class="abs foot-line" style="left:407px;top:2637px">
  <svg width="12" height="14" viewBox="0 0 24 28" fill="none" stroke="#1a9bd7" stroke-width="2"><path d="M12 26s8-9 8-15a8 8 0 0 0-16 0c0 6 8 15 8 15z"/><circle cx="12" cy="11" r="3"/></svg>
  <span style="font-size:10px">Lindenwood Plaza,<br>2280 Mercer Ave NE., # 214, Atlanta,<br>GA 30399</span>
</div>

<h3 class="abs foot-head script" style="left:668px">Quick Links</h3>
<ul class="abs foot-links"><li>Home</li><li>About Us</li><li>Services</li><li>Locations</li><li>Reviews</li><li>Contact Us</li></ul>

<h3 class="abs foot-head script" style="left:817px">Sign Up Newsletter</h3>
<p class="abs newsletter-text">There are many variations of passages lorem Ipsum available</p>
<div class="abs email-field">Enter your email ...</div>
<a class="abs btn send">Send</a>

<div class="abs divider"></div>
<p class="abs copy">© 2021 <b>Sudsy Harbor Atlanta</b> All Right Reserved</p>
<span class="abs social" style="left:819px;background:#0054aa" aria-label="Social link"></span>
<span class="abs social" style="left:850px;background:#1a9bd7" aria-label="Social link"></span>
<svg class="abs" style="left:1047px;top:2757px" width="18" height="24" viewBox="0 0 18 24" fill="none" stroke="#0054aa" stroke-width="1.6"><path d="M9 23V1M1 9l8-8 8 8"/></svg>

</body>
</html>
```